Vorna Fleet business card

I am needing a business card that at a glance shows all the services that we provide emphasizing some more than others. We are a Fleet and Compliance management company as well as a software company. We provide outsourced solutions for KPX compliance and HR services via our own software.
In addition, we do
drug testing
GPS
Cameras
Electronic DVIRS
ELD's

Target Market(s)

Transportation company owners

Industry/Entity Type

Transportation supplier

Contact Information for Business Card

the card should inform potential customers what we do

Other font styles liked:
• I have added brand guidelines. See attached

Requirements
Must have
• See description
Should not have
• Colors outside my brand guide. See attached

```html
<!DOCTYPE html>
<html lang="en">
<head>
<meta charset="utf-8">
<title>Vorna Fleet – Business Card</title>
<link href="https://fonts.googleapis.com/css2?family=Arimo:wght@400;700&display=swap" rel="stylesheet">
<style>
  :root {
    --page-bg: #e4e1dd;
    --card-bg: #f2f1ef;
    --ink: #2b2828;
    --ink-dark: #231f1f;
    --brand-red: #e11b22;
    --muted-light: #d9d3cd;
  }
  * { margin: 0; padding: 0; box-sizing: border-box; }
  html, body {
    width: 1200px; height: 897px; overflow: hidden;
    background: var(--page-bg);
    font-family: "Arimo", Arial, sans-serif;
  }
  .card {
    position: absolute; left: 75px; top: 163px;
    width: 1050px; height: 570px;
    border-radius: 22px; overflow: hidden;
    background: var(--card-bg);
  }
  .lower-band {
    position: absolute; left: 0; right: 0; top: 270px; bottom: 0;
    background: linear-gradient(to right, #c81d22 0%, #5a1c1d 30%, var(--ink-dark) 55%, var(--ink-dark) 100%);
  }
  .brand-name {
    position: absolute; left: 60px; top: 118px;
    font-size: 60px; font-weight: 700; color: var(--ink);
    letter-spacing: 1px; white-space: nowrap;
  }
  .services {
    position: absolute; left: 760px; top: 56px;
    list-style: none; color: var(--ink);
    font-size: 22px; line-height: 37px;
  }
  .services li span { margin-right: 16px; white-space: nowrap; }
  .services li span::before {
    content: "•"; color: var(--brand-red); margin-right: 6px; font-size: 16px;
  }
  .person {
    position: absolute; right: 50px; top: 300px; text-align: right;
  }
  .person-name {
    color: var(--brand-red); font-weight: 700; font-size: 35px; letter-spacing: 0.5px;
  }
  .person-title { color: var(--muted-light); font-size: 22px; margin-top: 6px; }
  .contacts {
    position: absolute; right: 50px; top: 412px; list-style: none; text-align: right;
    color: var(--muted-light); font-size: 22px;
  }
  .contacts li {
    display: flex; justify-content: flex-end; align-items: center;
    gap: 8px; height: 33px; white-space: nowrap;
  }
  .contact-icon { width: 25px; height: 25px; flex: none; }
</style>
</head>
<body>
  <main class="card">
    <div class="lower-band" role="img" aria-label="Decorative red and black wave band across the lower card"></div>

    <div class="brand-name">Vorna Fleet</div>

    <ul class="services">
      <li><span>Drug Testing</span><span>GPS</span></li>
      <li><span>Cameras</span><span>ELD's</span></li>
      <li><span>Electronic DVIRS</span></li>
    </ul>

    <div class="person">
      <div class="person-name">DELAN MARSH</div>
      <div class="person-title">CEO/Founder</div>
    </div>

    <ul class="contacts">
      <li>(555) 014-2290
        <svg class="contact-icon" viewBox="0 0 24 24" aria-hidden="true">
          <circle cx="12" cy="12" r="12" fill="var(--brand-red)"/>
          <path fill="#fff" d="M8.2,6.5 l2,2.3 -1.1,1.4 c0.8,1.8 2,3 3.8,3.8 l1.4,-1.1 2.3,2 -1.2,1.8 c-4.3,-0.4 -8.2,-4.3 -8.6,-8.6 Z"/>
        </svg>
      </li>
      <li>info@vornafleet.com
        <svg class="contact-icon" viewBox="0 0 24 24" aria-hidden="true">
          <circle cx="12" cy="12" r="12" fill="var(--brand-red)"/>
          <rect x="6" y="8" width="12" height="8.5" fill="#fff"/>
          <path d="M6,8 L12,13 L18,8" fill="none" stroke="var(--brand-red)" stroke-width="1.2"/>
        </svg>
      </li>
      <li>www.vornafleet.com
        <svg class="contact-icon" viewBox="0 0 24 24" aria-hidden="true">
          <circle cx="12" cy="12" r="12" fill="var(--brand-red)"/>
          <circle cx="12" cy="12" r="6" fill="none" stroke="#fff" stroke-width="1.3"/>
          <ellipse cx="12" cy="12" rx="2.6" ry="6" fill="none" stroke="#fff" stroke-width="1.1"/>
          <path d="M6,12 H18" stroke="#fff" stroke-width="1.1"/>
        </svg>
      </li>
    </ul>
  </main>
</body>
</html>
```